Search and Rescue Volunteer Profiles

We have 38 search and rescue volunteers and we need to create individual profile pages for an upcoming event. We want these to represent our brand and look similar to other work we have created but with new content. I have included a poster that we have used in the past to highlight volunteers (used for an ad campaign--which we aren't doing this time) but we want it changed up a bit. WE want their name, SR#, the year they joined the team and a few funny facts about them. This poster should show strength while also representing humanity (and a little humor). I'm picturing grid like background and strong colors. Also including our 25th anniversary logo which should be included.

```html
<!DOCTYPE html>
<html lang="en">
<head>
<meta charset="utf-8">
<title>Volunteer Profile – Marcus</title>
<link href="https://fonts.googleapis.com/css2?family=Montserrat:wght@400;500;700&display=swap" rel="stylesheet">
<style>
  :root {
    --red: #d22d46;
    --panel: #e4e2dd;
    --grid: rgba(28,28,28,.07);
    --ink: #1c1c1c;
    --rule: #b9b6b0;
    --page: #f2f1ee;
    --white: #ffffff;
  }
  * { margin: 0; padding: 0; box-sizing: border-box; }
  html, body { width: 1200px; height: 1200px; overflow: hidden; background: var(--page); }
  body { font-family: 'Montserrat', Arial, sans-serif; color: var(--ink); position: relative; }

  .poster { position: absolute; left: 211px; top: 50px; width: 778px; height: 1100px; overflow: hidden;
    background: var(--white); box-shadow: 0 4px 18px rgba(0,0,0,.18); }

  .portrait { position: absolute; left: 0; top: 0; width: 475px; height: 1100px;
    background:
      radial-gradient(ellipse 60% 38% at 45% 38%, #cfcfcf 0%, #9a9a9a 55%, transparent 80%),
      linear-gradient(180deg, #eeeeee 0%, #bdbdbd 28%, #6d6d6d 62%, #2a2a2a 100%); }

  .portrait-mark { position: absolute; left: 140px; top: 840px; width: 270px; text-align: center;
    font-weight: 700; font-size: 20px; line-height: 1.25; color: rgba(255,255,255,.55); letter-spacing: 1px; }

  .site-strip { position: absolute; left: 0; top: 1046px; width: 456px; height: 54px; background: rgba(242,241,238,.92); }
  .site-strip span { position: absolute; left: 38px; top: 16px; font-size: 17px; font-weight: 500; letter-spacing: 2px; color: var(--red); }

  .panel { position: absolute; left: 475px; top: 0; width: 303px; height: 1100px; background-color: var(--panel);
    background-image:
      linear-gradient(var(--grid) 1px, transparent 1px),
      linear-gradient(90deg, var(--grid) 1px, transparent 1px);
    background-size: 24px 24px; }

  .headline { position: absolute; right: 36px; text-align: right; color: var(--red); font-weight: 700; line-height: 1; white-space: nowrap; }
  .headline.pct { top: 38px; font-size: 104px; letter-spacing: -2px; }
  .headline.vol { top: 130px; font-size: 72px; letter-spacing: -1px; }

  .badge { position: absolute; left: 475px; top: 214px; width: 303px; height: 200px; }
  .badge-name { position: absolute; left: 552px; top: 286px; width: 140px; text-align: center;
    font-weight: 700; font-size: 15px; line-height: 1.3; color: var(--red); }

  .profile { position: absolute; right: 36px; text-align: right; }
  .profile-name { top: 432px; font-size: 29px; font-weight: 700; letter-spacing: 1px; }

  .stats { position: absolute; right: 36px; top: 476px; display: flex; gap: 8px; }
  .stat { width: 110px; height: 52px; background: var(--red); color: var(--white); text-align: center; padding-top: 7px; }
  .stat.dark { background: var(--ink); }
  .stat small { display: block; font-size: 11px; font-weight: 500; letter-spacing: 1.5px; }
  .stat strong { display: block; font-size: 20px; font-weight: 700; line-height: 24px; }

  .rule { position: absolute; height: 1px; background: var(--rule); }

  .bio { top: 556px; font-size: 16.5px; line-height: 22px; }
  .bio .caps { font-weight: 500; }

  .facts { top: 724px; font-size: 16.5px; line-height: 22px; }
  .facts .label { color: var(--red); font-weight: 700; letter-spacing: 1px; }

  .quote-mark { position: absolute; font-family: Georgia, serif; font-weight: 700; font-size: 30px; line-height: 1; color: var(--ink); }
  .quote { position: absolute; left: 517px; top: 852px; width: 230px; font-size: 16.5px; line-height: 22px; }

  .cta-bar { position: absolute; left: 456px; top: 1031px; width: 322px; height: 47px; background: var(--red);
    color: var(--white); font-weight: 700; font-size: 26px; text-align: center; line-height: 47px; }
</style>
</head>
<body>
  <main class="poster">
    <div class="portrait" role="img" aria-label="Black-and-white portrait photograph of volunteer Marcus in a fleece jacket with climbing gear"></div>
    <div class="portrait-mark">RIDGELINE COUNTY<br>SEARCH AND RESCUE</div>

    <div class="site-strip"><span>VOLUNTEER PROFILE</span></div>

    <section class="panel"></section>

    <div class="headline pct">100%</div>
    <div class="headline vol">volunteer</div>

    <svg class="badge" viewBox="0 0 303 200" aria-hidden="true">
      <polygon points="0,25 30,25 70,50 233,50 273,25 303,25 303,175 273,175 233,150 70,150 30,175 0,175" fill="#ffffff"/>
      <circle cx="147" cy="100" r="95" fill="#ffffff"/>
    </svg>
    <div class="badge-name">RIDGELINE COUNTY SEARCH AND RESCUE</div>

    <div class="profile profile-name">MARCUS</div>

    <div class="stats">
      <div class="stat"><small>SR#</small><strong>27</strong></div>
      <div class="stat dark"><small>JOINED</small><strong>2009</strong></div>
    </div>

    <div class="rule" style="left:526px; top:542px; width:223px;"></div>

    <div class="profile bio">
      <span class="caps">HUSBAND</span> to tessa,<br>
      <span class="caps">FATHER</span> to wren,<br>
      dog dad to <span class="caps">Scout &amp; Moss.</span><br>
      <span class="caps">ADDICTED</span> to <span class="caps">ice cream</span><br>
      and trail running. Life<br>
      Insurance &amp; Financial<br>
      Planning <span class="caps">ADVISOR.</span>
    </div>

    <div class="profile facts">
      <span class="label">FUNNY FACTS</span><br>
      Owns 14 headlamps.<br>
      Once out-ran a moose.<br>
      Still can’t fold a map.
    </div>

    <div class="quote-mark" style="left:494px; top:832px;">&ldquo;</div>
    <div class="rule" style="left:516px; top:843px; width:225px;"></div>
    <p class="quote">There is nothing more satisfying than reuniting a lost or injured person with their family.</p>
    <div class="rule" style="left:495px; top:960px; width:222px;"></div>
    <div class="quote-mark" style="left:720px; top:947px;">&rdquo;</div>

    <div class="cta-bar">Ridgelinesar.org</div>
  </main>
</body>
</html>
```